Experienced and Professional Marriage Celebrant

I need a web design for my services as a marriage celebrant in the Sydney area. I want people to have the impression I am a modern and professional marriage celebrant who can tailor a wedding ceremony and execute the ceremony with a high level of care and accommodate and adapt to any style of wedding and personalities of couples. I like a mint and pink and black theme and I am not sure whether to use the professional photos of me, might be too stiff! But would like to see ideas you can come up with. Happy to use other photos you might have

Reason: I have haven't been able to respond as quickly as I would have liked this last week to comments so extending a few days. Thanks

```html
<!DOCTYPE html>
<html lang="en">
<head>
<meta charset="utf-8">
<title>Mara Linden Celebrant</title>
<link rel="stylesheet" href="https://fonts.googleapis.com/css2?family=Arimo:wght@400;700&display=swap">
<style>
:root{
  --pink:#ff0a84;
  --pink-light:#ff4fa6;
  --mint:#9ee8cf;
  --navy:#1b4a6e;
  --white:#ffffff;
  --black:#000000;
  --grey:#8a8a8a;
  --frame:#ffffff;
}
*{box-sizing:border-box;margin:0;padding:0}
html,body{width:1000px;height:1200px;overflow:hidden}
body{position:relative;font-family:"Arimo",Arial,sans-serif;background:var(--white);color:var(--white)}
.hero-photo{position:absolute;left:0;top:0;width:1000px;height:1030px;
  background:linear-gradient(180deg,#6f97bd 0%,#7ea6c9 30%,#a7c2d8 46%,#4f6a3c 58%,#33472a 66%,#8a7866 74%,#c7a98b 86%,#d9c1a5 100%)}
.header-fade{position:absolute;left:0;top:0;width:1000px;height:90px;
  background:linear-gradient(180deg,#ffffff 0%,rgba(255,255,255,.85) 45%,rgba(255,255,255,0) 100%)}
.brand{position:absolute;left:50px;top:14px;font-size:32px;color:var(--navy);font-weight:400}
.call{position:absolute;left:749px;top:26px;font-size:18px;color:var(--black)}
.main-nav{position:absolute;left:65px;top:72px;width:870px;height:46px;background:var(--pink);
  box-shadow:0 3px 5px rgba(0,0,0,.45);display:flex;padding-left:91px}
.main-nav a{color:var(--white);text-decoration:none;font-size:24px;line-height:44px;padding:0 12px}
.main-nav a.active{background:var(--pink-light);padding:0 16px}
.intro-title{position:absolute;left:76px;top:143px;font-size:29px;font-weight:400}
.intro-rule{position:absolute;left:76px;top:185px;width:667px;height:2px;background:var(--mint)}
.intro-text{position:absolute;left:75px;top:205px;width:685px;font-size:24px;line-height:29px}
.photo-frame{position:absolute;left:766px;top:201px;width:184px;height:208px;background:var(--frame);
  box-shadow:0 2px 5px rgba(0,0,0,.4)}
.flower-photo{position:absolute;left:15px;top:17px;width:154px;height:174px;
  background:linear-gradient(135deg,#6b3a1c 0%,#e8806a 40%,#f2b39a 65%,#d9c7b6 100%)}
.testimonials{position:absolute;left:0;top:864px;width:1000px;height:162px;background:rgba(247,244,244,.9)}
.testimonials h2{position:absolute;left:0;width:1000px;top:21px;text-align:center;font-size:20px;font-weight:400;color:var(--pink)}
.review{position:absolute;top:21px;width:400px;height:140px}
.review .avatar{position:absolute;left:0;top:0;width:110px;height:110px;border-radius:50%;
  background:linear-gradient(160deg,#c9c4c2,#7a5444 60%,#3a2a26);box-shadow:0 1px 4px rgba(0,0,0,.4)}
.review .quote{position:absolute;left:124px;top:48px;width:240px;font-size:14px;line-height:17px;color:var(--grey)}
.review .who{position:absolute;left:3px;top:117px;font-size:14px;color:var(--pink)}
.pink-rule{position:absolute;left:0;top:1026px;width:1000px;height:9px;background:var(--pink)}
.site-footer{position:absolute;left:0;top:1035px;width:1000px;height:165px;background:var(--black)}
.portrait{position:absolute;left:108px;top:7px;width:104px;height:130px;background:linear-gradient(180deg,#2b2b2b,#6a5a6e 60%,#b79cc8)}
.portrait-name{position:absolute;left:108px;top:139px;width:104px;text-align:center;font-size:12px}
.foot-col{position:absolute;top:20px;font-size:18px;line-height:22px}
.foot-col a{color:var(--white);text-decoration:none;display:block}
.foot-heading{color:var(--mint)}
.follow{position:absolute;left:740px;top:20px;width:110px;text-align:center;font-size:18px;color:var(--mint)}
.social{position:absolute;left:771px;top:50px;display:flex;gap:6px}
.social span{width:11px;height:11px;background:var(--mint)}
</style>
</head>
<body>
<div class="hero-photo" role="img" aria-label="Wedding party walking hand in hand along a beach at sunset"></div>
<div class="header-fade"></div>

<div class="brand">Mara Linden Celebrant</div>
<div class="call">Call Us: 111-555-0188</div>

<nav class="main-nav">
  <a class="active" href="#">Home</a>
  <a href="#">About</a>
  <a href="#">Ceremony</a>
  <a href="#">Gallery</a>
  <a href="#">Testimonials</a>
  <a href="#">Contact</a>
</nav>

<h1 class="intro-title">Introduction</h1>
<div class="intro-rule"></div>
<p class="intro-text">Welcome! I am a modern, professional marriage celebrant serving couples across the Sydney area. Every ceremony I create is tailored to you, and delivered on the day with a high level of care. Grand or intimate, classic or relaxed, I adapt to any style of wedding and to the personalities of every couple. Let's talk about your ideas and shape a ceremony that feels truly yours.</p>

<div class="photo-frame">
  <div class="flower-photo" role="img" aria-label="Pink orchids in a glass vase on a reception table"></div>
</div>

<section class="testimonials">
  <h2>Tetimonials</h2>
  <div class="review" style="left:63px">
    <div class="avatar" role="img" aria-label="Portrait of a happy couple"></div>
    <p class="quote">Ms. Mara Linden is very professional<br>we are very happy</p>
    <div class="who">Mr. / Mrs. A &amp; B</div>
  </div>
  <div class="review" style="left:594px">
    <div class="avatar" role="img" aria-label="Portrait of a happy couple"></div>
    <p class="quote">Ms. Mara Linden is very professional<br>we are very happy</p>
    <div class="who">Mr. / Mrs. A &amp; B</div>
  </div>
</section>

<div class="pink-rule"></div>

<footer class="site-footer">
  <div class="portrait" role="img" aria-label="Portrait of the celebrant"></div>
  <div class="portrait-name">Mara Linden</div>
  <div class="foot-col" style="left:292px">
    <a href="#">Home</a><a href="#">About</a><a href="#">Ceremony</a><a href="#">Gallery</a>
  </div>
  <div class="foot-col" style="left:482px">
    <div class="foot-heading">Contact</div><div>111-555-0188</div><div>Address: Sydney</div><div>Email: mara@email.com</div>
  </div>
  <div class="follow">Follow Us</div>
  <div class="social"><span></span><span></span><span></span></div>
</footer>
</body>
</html>
```